Vocational Mentor needs an impressive business card

1. I need a business card (or maybe three with identic look) to promote me and my three business titles/services:
- Vocational Mentor. I help people find their vocation and live happily from it. I use my 20 years of experience in business, management and psychology to help them identify the most efficient ways to make a living doing what they are passionate about.
- Business Angel. I help founders start a succesful business with minimum risks and costs. I use my 20 years of experience in sales, management and entrepreneurship to help them identify the most efficient ways, in terms of time and cost, to validate their business idea.
- Learning Designer. I design unique learning programs that produce long-term cognitive and behavioural changes to people and organisations. I use my 20 years of experience in learning, teaching and change management to create minimalist experiences and processes that allow them to change efficiently in their pursued direction.

2. I would like a two-sided business card, on the front with my name, contact details and titles, on the back the explanation of the services.
Updates

Hi all,

I updated my brief, included contacts info and give feedback on all designs I got. I am new on this platform so please tell me if you need anything else or if I don't use corectly the platform forms.

Kind regards,
Tudor

Hi all,

I shortened the services description by deleting the phrase "I call..."

Kind regards,
Tudor

Target Market(s)

Freelancers, startups, people and organization willing to invest in change through ultimate learning experiences

Industry/Entity Type

Business

Font styles to use
Serif

Requirements
Must have
• Front side: full name, titles, web site, email, phone like below:
Tudor Vasilache
Vocational Mentor, Business Angel, Learning Designer
info@tudorvasilache.example
www.tudorvasilache.example
+40-745-TUDORV
Nice to have
• Back side: the description of the services I provide as in the task description.
1/3: it would be nice if I can jam all three titles on the front side but then I need a solution to jam all three services on the back side.

```html
<!DOCTYPE html>
<html lang="en">
<head>
<meta charset="utf-8">
<title>Tudor Vasilache — Business Card</title>
<link rel="stylesheet" href="https://fonts.googleapis.com/css2?family=Arimo:wght@400;700&display=swap">
<style>
  :root {
    --orange: #e36121;
    --blue: #0a8bd6;
    --white: #ffffff;
    --edge: #8fc9e8;
  }
  html, body {
    margin: 0;
    padding: 0;
    overflow: hidden;
    background: var(--white);
  }
  .canvas {
    position: relative;
    width: 933px;
    height: 1200px;
    overflow: hidden;
    background: var(--white);
    font-family: "Arimo", Arial, sans-serif;
  }
  .card-front, .card-back {
    position: absolute;
    left: 0;
    width: 933px;
  }
  .card-front { top: 0; height: 564px; }
  .card-back  { top: 635px; height: 565px; }
  .card-shape { position: absolute; inset: 0; }

  .name {
    position: absolute;
    left: 106px;
    top: 80px;
    margin: 0;
    font-size: 54px;
    font-weight: 700;
    line-height: 1;
    color: var(--blue);
    letter-spacing: 0.3px;
  }
  .name .surname { color: var(--orange); }
  .titles {
    position: absolute;
    left: 106px;
    top: 160px;
    margin: 0;
    font-size: 27px;
    color: var(--blue);
    line-height: 1;
  }
  .contact {
    position: absolute;
    margin: 0;
    font-size: 27px;
    color: var(--blue);
    line-height: 1;
  }
  .contact-web   { left: 92px;  top: 357px; }
  .contact-email { left: 480px; top: 357px; }
  .contact-phone { left: 0; width: 933px; text-align: center; top: 406px; }

  .services {
    position: absolute;
    left: 30px;
    top: 56px;
    width: 855px;
    font-size: 24.5px;
    line-height: 27.8px;
    color: var(--white);
  }
  .service { margin: 0; }
  .service + .service { margin-top: 56px; }
  .service:last-child { margin-top: 36px; text-align: justify; }
  .service-title { color: var(--blue); }
</style>
</head>
<body>
<div class="canvas">

  <section class="card-front">
    <svg class="card-shape" width="933" height="564" viewBox="0 0 933 564" aria-hidden="true">
      <rect width="933" height="564" fill="var(--orange)"/>
      <path d="M49,39 H885 Q905,39 905,59 V449 Q905,469 885,469 H245 Q221,469 221,490 V525 L212,525 L60,390 Q29,365 29,330 V59 Q29,39 49,39 Z" fill="var(--white)"/>
    </svg>
    <h1 class="name">Tudor <span class="surname">Vasilache</span></h1>
    <p class="titles">Vocational Mentor, Business Angel, Learning Designer</p>
    <p class="contact contact-web">www.tudorvasilache.example</p>
    <p class="contact contact-email">info@tudorvasilache.example</p>
    <p class="contact contact-phone">+40-745-TUDORV</p>
  </section>

  <section class="card-back">
    <svg class="card-shape" width="933" height="565" viewBox="0 0 933 565" aria-hidden="true">
      <rect x="0.5" y="0.5" width="932" height="564" fill="var(--orange)" stroke="var(--edge)" stroke-width="1"/>
      <rect x="897" y="0" width="6" height="565" fill="var(--blue)"/>
      <rect x="912" y="0" width="6" height="565" fill="var(--blue)"/>
    </svg>
    <div class="services">
      <p class="service"><span class="service-title">- Vocational Mentor.</span> I help people to find their vocation and live happily from it.<br>I use my 20 years of experience in business, management and psychology to<br>help them identify the most efficient ways to make a living doing what they are<br>passionate about.</p>
      <p class="service"><span class="service-title">- Business Angel.</span> I help founders to start a succesful business with minimum<br>risks and costs. I use my 20 years of experience in sales, management and<br>entrepreneurship to help them identify the most efficient ways, in terms of time<br>and cost, to validate their business idea.</p>
      <p class="service"><span class="service-title">- Learning Designer.</span> I design unique learning programs that produce long-term cognitive and behavioural changes to people and organisations. I use my 20 years of experience in learning, teaching and change management to create minimalist experiences and processes that allows them to change efficiently in their pursued direction.</p>
    </div>
  </section>

</div>
</body>
</html>
```